Conference program advertisement

Our business www.clinicledger.com.au is a good sponsor of the conference program run by the Southern Pacific Guild of Perioperative Physicians (SPGPP) here in Western Australia.
We have been running the same ad for a while and so we could do with a fresh new presence.
We have a conference banner and other signage that we'll use at the trade show so we're not looking to rebrand. Just looking for a new ad.
Specification is full colour A4, high res PDF
(Because I'm using my phone to create this job, I cannot seem to upload the existing ad. I'll do do ASAP.)

Target Market(s)

Specialist doctors

Industry/Entity Type

Trade

Font styles to use
Sans Serif

Colors

Designer to choose colors to be used in the design.

Requirements
Must have
• A4
Existing logo and colour scheme

```html
<!DOCTYPE html>
<html lang="en">
<head>
<meta charset="utf-8">
<title>Clinic Ledger Services – Conference Advertisement</title>
<link href="https://fonts.googleapis.com/css2?family=Oswald:wght@600;700&family=Open+Sans:wght@400;600;700;800&display=swap" rel="stylesheet">
<style>
:root{
  --navy:#0f5d9c;
  --blue:#2f93d3;
  --blue-deep:#1a74b8;
  --accent:#e0532c;
  --ink:#24323f;
  --card:#ffffff;
  --muted:#5a6b78;
  --icon-grey:#9aa8b3;
}
*{box-sizing:border-box;margin:0;padding:0}
html,body{width:849px;height:1200px;overflow:hidden;background:#fff}
.ad{position:relative;width:849px;height:1200px;overflow:hidden;background:#fff;font-family:"Open Sans",Arial,sans-serif;color:var(--ink)}
.hero-photo{position:absolute;left:400px;top:0;width:449px;height:520px;background:linear-gradient(135deg,#f4f8fb 0%,#dbe9f3 45%,#9cc6e4 80%,#5aa3d6 100%)}
.headline{position:absolute;left:70px;top:40px;font-family:"Oswald","Arial Narrow",sans-serif;font-weight:700;color:var(--navy);line-height:.95;text-transform:uppercase}
.headline span{display:block}
.headline .l1,.headline .l2,.headline .l4,.headline .l5{font-size:82px}
.headline .l2{color:var(--accent)}
.headline .l3{font-size:168px;line-height:.88}
.band{position:absolute;left:0;top:518px;width:849px;height:564px;background:var(--blue)}
.intro{position:absolute;left:70px;top:536px;width:710px;color:#fff;font-size:15px;line-height:1.5;text-align:center}
.callout{position:absolute;left:90px;top:666px;width:670px;color:#fff;font-weight:800;font-size:17px;line-height:1.35;text-align:center;text-transform:uppercase}
.mascot{position:absolute;left:12px;top:820px;width:220px;height:270px;border-radius:40px 40px 0 0;background:linear-gradient(180deg,#eef4f8 0%,#c9dbe8 100%)}
.services{position:absolute;left:240px;top:738px;width:585px;display:grid;grid-template-columns:repeat(3,1fr);grid-auto-rows:64px;gap:16px 10px;list-style:none}
.service{background:var(--card);border-radius:8px;display:flex;align-items:center;gap:10px;padding:0 10px;box-shadow:0 2px 4px rgba(0,0,0,.12)}
.service svg{flex:0 0 34px}
.service span{font-weight:800;font-size:13.5px;line-height:1.15;color:var(--accent);text-transform:uppercase}
.footer{position:absolute;left:0;top:1082px;width:849px;height:118px}
.site{position:absolute;left:30px;top:86px;font-weight:800;font-size:15px;color:var(--blue-deep);text-transform:uppercase}
.contact{position:absolute;left:270px;top:16px;font-size:11.5px;line-height:1.45;color:var(--ink);display:flex;gap:20px}
.contact .person{width:240px}
.contact .office{width:140px}
.contact strong{font-size:13px}
.brand{position:absolute;left:688px;top:18px;display:flex;align-items:center;gap:8px}
.brand .mark{width:30px;height:30px;flex:0 0 30px;background:var(--blue)}
.brand .name{font-weight:800;font-size:13px;line-height:1.1;color:var(--blue-deep);text-transform:uppercase}
.brand .tag{font-size:10px;color:var(--muted);margin-top:2px}
.social{position:absolute;left:726px;top:88px;display:flex;gap:6px}
.social i{display:block;width:16px;height:16px;background:var(--icon-grey)}
</style>
</head>
<body>
<div class="ad">
  <div class="hero-photo" role="img" aria-label="Photo of a doctor in scrubs with a stethoscope holding up a small alarm clock"></div>

  <h1 class="headline">
    <span class="l1">Is admin</span>
    <span class="l2">eating up</span>
    <span class="l3">Your</span>
    <span class="l4">valuable</span>
    <span class="l5">time?</span>
  </h1>

  <div class="band"></div>
  <p class="intro">Admin can consume a large amount of time for doctors working in private practice. From generating accounts to chasing up bad debts, from sitting on hold with health funds, or trawling through remittance advices to getting accreditation papers and submitting provider number applications properly – we're sure you would prefer to focus on being a doctor rather than worrying about paperwork and piles of admin.</p>
  <p class="callout">Clinic Ledger Services is here to help – contact us today if you're ready to remove the burden of admin.</p>

  <div class="mascot" role="img" aria-label="Cartoon illustration of a friendly doctor in a white coat"></div>

  <ul class="services">
    <li class="service"><svg width="34" height="34" viewBox="0 0 34 34"><circle cx="17" cy="17" r="16" fill="#2f93d3"/><path d="M10 12h14v10H10z" fill="none" stroke="#fff" stroke-width="2"/><path d="M10 16h14" stroke="#fff" stroke-width="2"/></svg><span>Private billing</span></li>
    <li class="service"><svg width="34" height="34" viewBox="0 0 34 34"><circle cx="17" cy="17" r="16" fill="#e0532c"/><path d="M11 11h12v13H11z" fill="none" stroke="#fff" stroke-width="2"/><path d="M14 15h6M14 19h6" stroke="#fff" stroke-width="2"/></svg><span>Cover lists</span></li>
    <li class="service"><svg width="34" height="34" viewBox="0 0 34 34"><circle cx="17" cy="17" r="16" fill="#2f93d3"/><path d="M10 18l5 5 9-11" fill="none" stroke="#fff" stroke-width="2.5"/></svg><span>Electronic claiming to health funds</span></li>
    <li class="service"><svg width="34" height="34" viewBox="0 0 34 34"><circle cx="17" cy="17" r="16" fill="#e0532c"/><path d="M11 22V12l6 6 6-6v10" fill="none" stroke="#fff" stroke-width="2"/></svg><span>VMP billing</span></li>
    <li class="service"><svg width="34" height="34" viewBox="0 0 34 34"><circle cx="17" cy="17" r="16" fill="#2f93d3"/><path d="M11 12h12M11 17h12M11 22h12" stroke="#fff" stroke-width="2"/></svg><span>Organise lists</span></li>
    <li class="service"><svg width="34" height="34" viewBox="0 0 34 34"><circle cx="17" cy="17" r="16" fill="#e0532c"/><path d="M17 9v16M13 13h6a3 3 0 010 6h-4a3 3 0 000 6h6" fill="none" stroke="#fff" stroke-width="2"/></svg><span>Fee estimates and informed financial consent</span></li>
    <li class="service"><svg width="34" height="34" viewBox="0 0 34 34"><circle cx="17" cy="17" r="16" fill="#2f93d3"/><path d="M11 24V16M17 24V10M23 24V14" stroke="#fff" stroke-width="3"/></svg><span>GST reporting</span></li>
    <li class="service"><svg width="34" height="34" viewBox="0 0 34 34"><circle cx="17" cy="17" r="16" fill="#e0532c"/><path d="M17 10v14M10 17h14" stroke="#fff" stroke-width="3"/></svg><span>Practice management</span></li>
    <li class="service"><svg width="34" height="34" viewBox="0 0 34 34"><circle cx="17" cy="17" r="16" fill="#2f93d3"/><path d="M17 10v14M10 17h14" stroke="#fff" stroke-width="3"/></svg><span>Medicare &amp; health fund registrations</span></li>
    <li class="service"><svg width="34" height="34" viewBox="0 0 34 34"><circle cx="17" cy="17" r="16" fill="#e0532c"/><path d="M10 22h14L17 10z" fill="none" stroke="#fff" stroke-width="2"/></svg><span>Banking</span></li>
    <li class="service"><svg width="34" height="34" viewBox="0 0 34 34"><circle cx="17" cy="17" r="16" fill="#2f93d3"/><rect x="9" y="12" width="16" height="11" rx="2" fill="none" stroke="#fff" stroke-width="2"/><path d="M9 16h16" stroke="#fff" stroke-width="2"/></svg><span>BPAY and credit card payments</span></li>
    <li class="service"><svg width="34" height="34" viewBox="0 0 34 34"><circle cx="17" cy="17" r="16" fill="#e0532c"/><path d="M11 10h12v14H11z" fill="none" stroke="#fff" stroke-width="2"/><path d="M14 17l2 2 4-4" fill="none" stroke="#fff" stroke-width="2"/></svg><span>Hospital accreditations</span></li>
  </ul>

  <footer class="footer">
    <div class="contact">
      <div class="person"><strong>Liam Harcourt</strong> Mobile +61 400 555 182<br>Office 08 6100 4127 • Fax 08 6100 4128<br>Level 2, 14 Harbour View Road, West Perth</div>
      <div class="office">Ground Floor, Unit 12,<br>77 Marlow Street<br>West Perth, WA, 6005</div>
    </div>
    <div class="brand">
      <div class="mark"></div>
      <div><div class="name">Clinic Ledger<br>Services</div><div class="tag">trusted practice admin</div></div>
    </div>
    <div class="social"><i></i><i></i><i></i></div>
    <div class="site">www.clinicledger.com.au</div>
  </footer>
</div>
</body>
</html>
```